Copper Gate Labradoodle web design

We're a new labradoodle breeder in Charleston, SC in need of a web design.

Our name is Copper Gate Labradoodles.

Site we like: http://www.fernhilldoodlery.example/
http://www.quailbrookpups.example/

Logo Font:
The ''Copper Gate'' font is called TestarossaNF and is available freely at http://www.typequarry.example/testarossa-nf.font.  The ''Labradoodles'' font is called Worstveld Sling Extra and is available freely at http://www.glyphbarn.example/WorstveldSlingExtra.php.

Requirements
Must have
• Our logo
1. Home page
2. Labradoodle F.A.Q.
3. Our doodles
4. Availability
5. Adoption Process
6. Contact us
Link/badge icon for Health Guarantee
Nice to have
• Color and font to match the logo.

An area to add pictures
Should not have
• Rainbows
Rainbow colors

```html
<!DOCTYPE html>
<html lang="en">
<head>
<meta charset="utf-8">
<title>Copper Gate Labradoodles</title>
<link rel="stylesheet" href="https://fonts.googleapis.com/css2?family=Federo&family=Open+Sans:wght@400;600&display=swap">
<style>
  :root {
    --pink: #e4a1b4;
    --pink-light: #f6d6e0;
    --pink-deep: #c9516f;
    --rose: #b23a58;
    --taupe: #b1a39b;
    --taupe-light: #d3c7bf;
    --taupe-pale: #eee9e5;
    --ink: #1c1416;
    --body: #3a3033;
    --white: #ffffff;
    --card: #f3f1f0;
  }
  * { box-sizing: border-box; margin: 0; padding: 0; }
  html, body { width: 1113px; height: 1200px; overflow: hidden; }
  body {
    position: relative;
    background: var(--pink);
    font-family: "Open Sans", sans-serif;
    color: var(--body);
  }
  .abs { position: absolute; }

  .top-rule { left: 0; top: 3px; width: 100%; height: 3px; background: var(--pink-deep); }
  .lace-band { left: 0; top: 406px; width: 100%; height: 625px; background: var(--pink-light); }
  .foot-rule { left: 0; top: 1029px; width: 100%; height: 3px; background: var(--pink-deep); }

  .brand { left: 152px; top: 14px; width: 162px; height: 150px; display: flex; flex-direction: column; align-items: center; justify-content: center; gap: 8px; }
  .brand-dot { width: 92px; height: 92px; border-radius: 50%; background: var(--white); }
  .brand-name { font-family: "Federo", sans-serif; font-size: 15px; color: var(--rose); text-align: center; line-height: 1.1; }

  .nav { left: 344px; top: 34px; width: 621px; height: 56px; background: var(--taupe-light); box-shadow: 2px 3px 4px rgba(0,0,0,.25); border-top: 6px solid var(--taupe); }
  .nav-home { left: 344px; top: 24px; width: 84px; height: 66px; background: linear-gradient(#f4eeea, #e3d9d2); border-top: 8px solid #ee8aa3; display: flex; align-items: center; justify-content: center; font-family: "Federo", sans-serif; font-size: 12px; color: var(--ink); font-weight: bold; box-shadow: 2px 0 3px rgba(0,0,0,.2); }
  .nav-links { left: 436px; top: 56px; width: 520px; display: flex; justify-content: space-between; font-family: "Federo", sans-serif; font-size: 12px; color: var(--white); letter-spacing: .5px; }
  .nav-links span + span { border-left: 1px dotted #f2ebe7; padding-left: 8px; }

  .hero { left: 342px; top: 106px; width: 342px; height: 300px; background: radial-gradient(ellipse at 55% 45%, #fbfaf7 0 48%, rgba(240,235,228,.6) 62%, rgba(228,161,180,0) 75%); }

  .panel { left: 149px; top: 406px; width: 815px; height: 710px; background: var(--white); }

  .welcome { left: 174px; top: 432px; font-family: "Federo", sans-serif; font-size: 18px; color: var(--ink); font-weight: bold; letter-spacing: .3px; }
  .welcome em { font-style: normal; color: var(--rose); }
  .rule { height: 1px; background: var(--ink); }
  .photo-main { left: 173px; top: 489px; width: 209px; height: 132px; background: linear-gradient(120deg, #6f5c50, #b9b2ad 55%, #e8e6e3); box-shadow: 2px 2px 4px rgba(0,0,0,.3); border: 2px solid #fff; }
  .copy { font-size: 10.6px; line-height: 16.3px; color: var(--body); letter-spacing: .3px; }
  .copy-side { left: 410px; top: 485px; width: 300px; }
  .copy-full { left: 173px; top: 636px; width: 540px; }
  .more-link { font-family: "Federo", sans-serif; font-size: 12px; color: var(--rose); font-weight: bold; letter-spacing: .5px; }

  .card { top: 757px; width: 173px; height: 309px; background: linear-gradient(var(--card), #fbfafa); text-align: center; }
  .card-photo { width: 100%; height: 115px; border-top: 6px solid #bdb6b2; }
  .card-photo.featured { border-top-color: var(--rose); }
  .card-title { height: 48px; margin-top: 12px; display: flex; align-items: center; justify-content: center; font-family: "Federo", sans-serif; font-size: 15px; color: #9d9590; line-height: 17px; letter-spacing: .6px; }
  .card-text { font-size: 9.6px; line-height: 16.3px; color: var(--body); padding: 0 8px; letter-spacing: .2px; }
  .card-btn { position: absolute; left: 34px; top: 259px; width: 99px; height: 30px; background: var(--taupe-light); box-shadow: 2px 2px 3px rgba(0,0,0,.3); font-family: "Federo", sans-serif; font-size: 11px; color: var(--white); font-weight: bold; line-height: 30px; }

  .contact { left: 746px; top: 429px; width: 196px; height: 286px; background: var(--taupe-light); box-shadow: 2px 3px 4px rgba(0,0,0,.25); }
  .contact-head { height: 44px; background: var(--taupe); display: flex; align-items: center; gap: 14px; padding-left: 20px; font-family: "Federo", sans-serif; font-size: 18px; color: var(--white); font-weight: bold; }
  .field { position: absolute; left: 9px; width: 176px; height: 27px; background: var(--white); border-radius: 3px; font-size: 10px; color: var(--ink); padding: 6px 7px; letter-spacing: .4px; }
  .submit { position: absolute; left: 93px; top: 243px; width: 92px; height: 26px; background: linear-gradient(#fff, #eee); border-radius: 3px; box-shadow: 1px 1px 2px rgba(0,0,0,.3); font-size: 12px; color: var(--ink); text-align: center; line-height: 26px; overflow: hidden; }
  .submit::before { content: ""; position: absolute; left: 0; bottom: 0; border-left: 10px solid #ee8aa3; border-top: 10px solid transparent; }

  .videos { left: 750px; top: 748px; font-family: "Federo", sans-serif; font-size: 20px; color: var(--ink); font-weight: bold; letter-spacing: .5px; }
  .video { left: 746px; width: 197px; height: 121px; border: 3px solid var(--taupe-light); display: flex; align-items: center; justify-content: center; }
  .video-a { top: 796px; background: linear-gradient(135deg, #c7c4c2, #e5d7b8 55%, #d7d3d0); }
  .video-b { top: 925px; background: linear-gradient(135deg, #7c6d58, #efe6c9 50%, #d6c9a5); }

  .foot-mark { left: 163px; top: 1128px; width: 57px; height: 52px; border-radius: 50%; background: var(--pink-light); }
  .foot-text { left: 231px; top: 1149px; font-size: 12.5px; color: var(--white); letter-spacing: .8px; }
  .social { left: 835px; top: 1141px; width: 31px; height: 31px; border-radius: 4px; background: #4a6fb3; }
  .badge { left: 882px; top: 1127px; width: 59px; height: 59px; border-radius: 50%; background: #e8c52a; }
</style>
</head>
<body>
  <div class="abs top-rule"></div>
  <div class="abs lace-band"></div>
  <div class="abs foot-rule"></div>

  <div class="abs brand">
    <div class="brand-dot"></div>
    <div class="brand-name">Copper Gate Labradoodles</div>
  </div>

  <div class="abs nav"></div>
  <div class="abs nav-home">HOME</div>
  <nav class="abs nav-links">
    <span>F.A.Q.</span><span>OUR DOODLES</span><span>AVAILABILITY</span><span>ADOPTION PROCESS</span><span>CONTACTS</span>
  </nav>

  <div class="abs hero" role="img" aria-label="White labradoodle smiling, cut out against the pink header"></div>

  <div class="abs panel"></div>

  <h1 class="abs welcome">WELCOME <em>COPPER GATE LABRADOODLES</em></h1>
  <div class="abs rule" style="left:171px;top:467px;width:535px"></div>

  <div class="abs photo-main" role="img" aria-label="Grey labradoodle resting its head on a blanket"></div>
  <p class="abs copy copy-side">Lorem Ipsum is simply dummy text of the printing and typesetting industry. Lorem Ipsum has been the industry's standard dummy text ever since the 1500s, when an unknown printer took a galley of type and scrambled it to make a type specimen book. It has survived not only five centuries, but also the leap into electronic typesetting, remaining essentially unchanged. It was popularised in the 1960s with the release of Letraset sheets containing Lorem Ipsum</p>
  <p class="abs copy copy-full">Lorem Ipsum is simply dummy text of the printing and typesetting industry. Lorem Ipsum has been the industry's standard dummy text ever since the 1500s, when an unknown printer took a galley of type and scrambled it to make a type specimen book.</p>
  <a class="abs more-link" style="left:173px;top:698px">READ MORE &gt;&gt;</a>

  <section class="abs card" style="left:171px">
    <div class="card-photo featured" role="img" aria-label="Golden labradoodle sitting in tall grass" style="background:linear-gradient(135deg,#b89a5c,#c97d33 50%,#d8c79a)"></div>
    <h2 class="card-title">HEALTH<br>GUARANTEE</h2>
    <p class="card-text">Lorem Ipsum is simply dummy text of the printing and typesetting industry. Lorem Ipsum has been the industry's</p>
    <div class="card-btn">MORE</div>
  </section>
  <section class="abs card" style="left:355px">
    <div class="card-photo" role="img" aria-label="Red labradoodle lying on a white seat" style="background:linear-gradient(135deg,#c9ccd3,#a4521f 50%,#e7e8ec)"></div>
    <h2 class="card-title">PUPPY<br>APPLICATION</h2>
    <p class="card-text">Lorem Ipsum is simply dummy text of the printing and typesetting industry. Lorem Ipsum has been the industry's</p>
    <div class="card-btn">MORE</div>
  </section>
  <section class="abs card" style="left:541px">
    <div class="card-photo" role="img" aria-label="Two cream labradoodle puppies in a wooden box" style="background:linear-gradient(#e9e6e1,#f1ece4 60%,#a8773a)"></div>
    <h2 class="card-title">BLOG</h2>
    <p class="card-text">Lorem Ipsum is simply dummy text of the printing and typesetting industry. Lorem Ipsum has been the industry's</p>
    <div class="card-btn">MORE</div>
  </section>

  <form class="abs contact">
    <div class="contact-head">
      <svg width="30" height="22" viewBox="0 0 30 22" aria-hidden="true">
        <rect x="1" y="6" width="28" height="15" rx="2" fill="#fff"/>
        <path d="M1 8 L15 16 L29 8" fill="none" stroke="#b1a39b" stroke-width="1.5"/>
        <path d="M4 6 L15 1 L26 6" fill="none" stroke="#fff" stroke-width="2"/>
      </svg>
      <span>Contact</span>
    </div>
    <div class="field" style="top:61px">Name:</div>
    <div class="field" style="top:97px">Email Address:</div>
    <div class="field" style="top:134px">Phone Number:</div>
    <div class="field" style="top:171px;height:61px">Comment:</div>
    <div class="submit">Submit</div>
  </form>

  <h2 class="abs videos">VIDEOS</h2>
  <div class="abs rule" style="left:746px;top:787px;width:196px"></div>

  <div class="abs video video-a" role="img" aria-label="Video still of two cream labradoodles lying together">
    <svg width="52" height="52" viewBox="0 0 52 52" aria-hidden="true">
      <circle cx="26" cy="26" r="24" fill="#8f8d8b" stroke="#d7d5d3" stroke-width="3"/>
      <path d="M20 14 L38 26 L20 38 Z" fill="#f4f4f4"/>
    </svg>
  </div>
  <div class="abs video video-b" role="img" aria-label="Video still of a shaggy cream labradoodle outdoors">
    <svg width="52" height="52" viewBox="0 0 52 52" aria-hidden="true">
      <circle cx="26" cy="26" r="24" fill="#8f8d8b" stroke="#d7d5d3" stroke-width="3"/>
      <path d="M20 14 L38 26 L20 38 Z" fill="#f4f4f4"/>
    </svg>
  </div>
  <a class="abs more-link" style="left:746px;top:1056px">MORE &gt;&gt;</a>

  <div class="abs foot-mark"></div>
  <p class="abs foot-text">COPPER GATE LABRADOODLES © 2013 | PRIVACY POLICY</p>
  <div class="abs social"></div>
  <div class="abs badge"></div>
</body>
</html>
```